Corporate Word-document templates

We need these documents templates for the following types of documentation:

- Proposal
- Report (meetings)
- Solution description (technical)
- Documentation

The front page of the documents can take inspiration from our PowerPoint template, website (https://www.lindqor.com/) and brand book. It should reflect our new branding guidelines.

See attached documents for structure and what we need them to contain. We need:
- front page
- generalt tekst page after the front page
- table of contents
- logo in upper right corner, page number + info in the footer, structure of tables
- anything else?

1) Make a design suggestion for the front page of the proposal and the Documentation
2) When we agree on the structure and front page, make the other two documents
3) we need all four documents with four different logos. 4 x 4 documents. the logos are: Marvelund, MVL, MVL Horizon & MVL Lens.

Target Market(s)

Large and medium corporations. Roles such as CEO, CFO, CIO, CTO, Controllers, Analysts, leaders/managers

Industry/Entity Type

Information Technology

Font styles to use
Sans Serif

Requirements
Must have
• - elements that are key to a word template
- four different word template files - each with the four different logos
- chose colors from our brand book

```html
<!DOCTYPE html>
<html lang="en">
<head>
<meta charset="utf-8">
<title>Marvelund – Document Templates</title>
<link href="https://fonts.googleapis.com/css2?family=Montserrat:wght@500;600;700;800&family=Arimo:wght@400;700&display=swap" rel="stylesheet">
<style>
:root{
  --navy:#173f73;
  --navy-deep:#13335e;
  --blue:#1f5c9c;
  --teal:#1b7f9d;
  --teal-light:#2b9bb6;
  --ring:#15598a;
  --disc:#7fb4cb;
  --ink:#2b2b2b;
  --rule:#1f4f86;
  --row-alt:#eef1f5;
  --stage-top:#9d9d9d;
  --stage-bottom:#a9a9a9;
  --paper:#ffffff;
}
*{box-sizing:border-box;margin:0;padding:0}
html,body{width:1200px;height:3557px;overflow:hidden}
body{position:relative;background:var(--stage-bottom);font-family:"Arimo",Arial,sans-serif;color:var(--ink)}
.stage-top{position:absolute;left:0;top:0;width:1200px;height:1125px;background:var(--stage-top)}

/* ---------- Cover ---------- */
.cover{position:absolute;width:522px;height:737px;background:var(--paper);overflow:hidden;box-shadow:0 4px 14px rgba(0,0,0,.25);transform-origin:0 0}
.cover--hero{left:327px;top:177px;transform:scale(1.08)}
.cover--spread{left:61px;top:1194px}
.cover__brand{position:absolute;top:0;left:0;width:100%;height:140px;display:flex;align-items:center;justify-content:center;font-family:"Montserrat",sans-serif;font-weight:800;font-size:54px;color:var(--navy);letter-spacing:-1px}
.cover__rule{position:absolute;left:0;top:140px;width:100%;height:7px;background:var(--navy)}
.cover__title-band{position:absolute;left:0;top:155px;width:100%;height:240px;background:linear-gradient(180deg,var(--navy-deep),#1d4f82)}
.cover__title{position:absolute;left:30px;top:58px;color:#fff;font-family:"Montserrat",sans-serif;font-weight:700;line-height:1;white-space:nowrap}
.cover__title span{display:block}
.cover__title .l1{font-size:50px}
.cover__title .l2{font-size:70px;margin-top:4px}
.cover__strip{position:absolute;left:0;width:100%;background:#fff;color:var(--navy);font-family:"Montserrat",sans-serif;font-weight:600;font-size:17px;text-align:center}
.cover__strip--top{top:395px;height:32px;line-height:32px}
.cover__strip--bottom{top:622px;height:30px;line-height:30px}
.cover__services{position:absolute;left:0;top:427px;width:100%;height:195px;background:linear-gradient(180deg,var(--teal),#1c7592)}
.cover__foot{position:absolute;left:0;top:652px;width:100%;height:85px;background:linear-gradient(180deg,#1c7592,var(--teal-light))}
.service{position:absolute;top:32px;width:150px;margin-left:-75px;text-align:center;color:#fff;font-family:"Montserrat",sans-serif;font-weight:600;font-size:17px}
.service svg{display:block;margin:0 auto 12px}
.service--plan{left:88px}
.service--analysis{left:261px}
.service--exec{left:430px}

/* ---------- Inner pages ---------- */
.page{position:absolute;width:522px;height:737px;background:var(--paper);box-shadow:0 4px 14px rgba(0,0,0,.22);overflow:hidden}
.page--p2{left:610px;top:1194px}
.page--p3{left:61px;top:1961px}
.page--p4{left:610px;top:1961px}
.page--p5{left:61px;top:2725px}
.page--p6{left:610px;top:2725px}
.page__header{position:absolute;left:35px;right:35px;top:30px;height:24px;display:flex;align-items:center;gap:10px}
.page__header-line{flex:1;height:1px;background:var(--rule)}
.page__brand{font-family:"Montserrat",sans-serif;font-weight:800;font-size:21px;color:var(--navy);letter-spacing:-.5px}
.page__footer{position:absolute;left:35px;right:35px;bottom:22px;height:20px;border-top:1px solid var(--rule);display:flex;align-items:flex-end;justify-content:space-between}
.page__web{display:flex;align-items:center;gap:6px;font-size:10px;letter-spacing:.5px;color:#333;padding-top:6px}
.page__num{width:20px;height:22px;background:var(--navy);color:#fff;font-size:11px;display:flex;align-items:center;justify-content:center;margin-bottom:-2px}
.page__body{position:absolute;left:52px;right:52px;top:84px}
.heading{font-family:"Montserrat",sans-serif;font-weight:700;font-size:23px;color:var(--blue)}
.subheading{font-family:"Arimo",sans-serif;font-weight:700;font-size:15px;color:var(--blue);margin-top:18px}
.copy{font-size:9.6px;line-height:1.32;text-align:justify;margin-top:16px}

/* page 2 */
.photo{position:absolute}
.photo--desk{left:0;top:0;width:207px;height:690px;background:linear-gradient(160deg,#8a5a3c 0%,#c7b8a8 35%,#e8e6e3 60%,#9aa3ad 100%)}
.photo--paper{left:217px;top:253px;width:305px;height:231px;background:linear-gradient(120deg,#d9dadc 0%,#a8acb3 55%,#3b3e44 100%)}
.p2-text{position:absolute;left:220px;width:268px;font-size:12.2px;line-height:1.3;text-align:justify}
.p2-text--a{top:104px}
.p2-text--b{top:512px}

/* page 3 TOC */
.toc-title{position:absolute;left:75px;top:103px;font-family:"Montserrat",sans-serif;font-weight:700;font-size:22px;color:var(--blue)}
.toc-title::after{content:"";display:block;width:115px;height:3px;background:var(--blue);margin-top:8px}
.toc{position:absolute;left:75px;top:164px;width:360px;list-style:none}
.toc li{display:flex;align-items:center;height:26px;font-size:13.5px}
.toc li .t{width:146px}
.toc li.sub .t{padding-left:13px}
.toc li.main{font-weight:700}
.toc li.gap{margin-top:12px}
.toc li .lead{width:136px;border-bottom:1px dashed #9aa;height:0;margin-top:2px}
.toc li .n{margin-left:auto;width:30px;text-align:center}

/* page 4 */
.block{margin-top:16px}
.block__tag{display:inline-block;background:var(--blue);color:#fff;font-size:9.6px;font-weight:700;padding:3px 12px}
.block__body{border-left:1px solid var(--blue);padding:6px 0 2px 14px;font-size:9.4px;line-height:1.3}
.block__body ul{list-style:none;margin-top:4px}
.block__body ul li{position:relative;padding-left:9px;margin-bottom:4px}
.block__body ul li::before{content:"";position:absolute;left:0;top:5px;width:3px;height:3px;border-radius:50%;background:var(--blue)}
.block__body p+ul{margin-top:10px}

/* page 5 table */
.table-wrap{margin-top:22px;border-top:1px solid var(--blue)}
.table-tag{display:inline-block;background:var(--blue);color:#fff;font-size:9.6px;font-weight:700;padding:4px 17px}
.data-table{width:100%;border-collapse:separate;border-spacing:2px;margin-top:3px;font-size:9.6px}
.data-table th{background:var(--blue);color:#fff;font-weight:700;height:24px;text-align:left;padding-left:12px}
.data-table td{height:24px;padding-left:12px;color:#444}
.data-table tr:nth-child(even) td{background:var(--row-alt)}
.copy--after{margin-top:30px}

/* page 6 info panel */
.info-panel{margin-top:34px;height:284px;background:var(--blue);display:flex;padding:16px 0}
.info-panel__col{flex:1;padding:0 14px;text-align:center;color:#fff;font-weight:700;font-size:10.2px;line-height:1.22}
.info-panel__col+.info-panel__col{border-left:1px dashed rgba(255,255,255,.7)}
.info-panel__col svg{display:block;margin:0 auto 10px}
</style>
</head>
<body>
<div class="stage-top"></div>

<!-- Hero cover -->
<section class="cover cover--hero">
  <div class="cover__brand">Marvelund</div>
  <div class="cover__rule"></div>
  <div class="cover__title-band">
    <h1 class="cover__title"><span class="l1">Unleash Business</span><span class="l2">Value Faster</span></h1>
  </div>
  <div class="cover__strip cover__strip--top">USER-FRIENDLY &amp; EFFECTIVE SOLUTIONS FOR</div>
  <div class="cover__services">
    <div class="service service--plan">
      <svg width="110" height="110" viewBox="0 0 110 110"><circle cx="55" cy="55" r="54" fill="var(--ring)"/><circle cx="55" cy="55" r="44" fill="var(--disc)"/><rect x="38" y="30" width="32" height="42" rx="3" fill="#fff"/><rect x="47" y="26" width="14" height="7" rx="2" fill="#fff" stroke="var(--disc)"/><g stroke="var(--disc)" stroke-width="3"><line x1="44" y1="44" x2="64" y2="44"/><line x1="44" y1="52" x2="64" y2="52"/><line x1="44" y1="60" x2="58" y2="60"/></g><rect x="32" y="70" width="46" height="8" rx="3" fill="#fff"/></svg>
      PLANNING
    </div>
    <div class="service service--analysis">
      <svg width="110" height="110" viewBox="0 0 110 110"><circle cx="55" cy="55" r="54" fill="var(--ring)"/><circle cx="55" cy="55" r="44" fill="var(--disc)"/><circle cx="51" cy="51" r="18" fill="none" stroke="#fff" stroke-width="6"/><line x1="64" y1="64" x2="76" y2="76" stroke="#fff" stroke-width="8" stroke-linecap="round"/><g fill="#fff"><rect x="43" y="50" width="4" height="9"/><rect x="49" y="44" width="4" height="15"/><rect x="55" y="47" width="4" height="12"/></g></svg>
      ANALYSIS
    </div>
    <div class="service service--exec">
      <svg width="110" height="110" viewBox="0 0 110 110"><circle cx="55" cy="55" r="54" fill="var(--ring)"/><circle cx="55" cy="55" r="44" fill="var(--disc)"/><circle cx="47" cy="46" r="13" fill="none" stroke="#fff" stroke-width="7" stroke-dasharray="5 3"/><circle cx="47" cy="46" r="5" fill="#fff"/><rect x="55" y="56" width="20" height="20" fill="none" stroke="#fff" stroke-width="4"/><rect x="60" y="61" width="10" height="10" fill="#fff"/></svg>
      EXECUTION
    </div>
  </div>
  <div class="cover__strip cover__strip--bottom">ALL GATHERED IN ONE PLACE</div>
  <div class="cover__foot"></div>
</section>

<!-- Spread cover -->
<section class="cover cover--spread">
  <div class="cover__brand">Marvelund</div>
  <div class="cover__rule"></div>
  <div class="cover__title-band">
    <h2 class="cover__title"><span class="l1">Unleash Business</span><span class="l2">Value Faster</span></h2>
  </div>
  <div class="cover__strip cover__strip--top">USER-FRIENDLY &amp; EFFECTIVE SOLUTIONS FOR</div>
  <div class="cover__services">
    <div class="service service--plan">
      <svg width="110" height="110" viewBox="0 0 110 110"><circle cx="55" cy="55" r="54" fill="var(--ring)"/><circle cx="55" cy="55" r="44" fill="var(--disc)"/><rect x="38" y="30" width="32" height="42" rx="3" fill="#fff"/><rect x="47" y="26" width="14" height="7" rx="2" fill="#fff" stroke="var(--disc)"/><g stroke="var(--disc)" stroke-width="3"><line x1="44" y1="44" x2="64" y2="44"/><line x1="44" y1="52" x2="64" y2="52"/><line x1="44" y1="60" x2="58" y2="60"/></g><rect x="32" y="70" width="46" height="8" rx="3" fill="#fff"/></svg>
      PLANNING
    </div>
    <div class="service service--analysis">
      <svg width="110" height="110" viewBox="0 0 110 110"><circle cx="55" cy="55" r="54" fill="var(--ring)"/><circle cx="55" cy="55" r="44" fill="var(--disc)"/><circle cx="51" cy="51" r="18" fill="none" stroke="#fff" stroke-width="6"/><line x1="64" y1="64" x2="76" y2="76" stroke="#fff" stroke-width="8" stroke-linecap="round"/><g fill="#fff"><rect x="43" y="50" width="4" height="9"/><rect x="49" y="44" width="4" height="15"/><rect x="55" y="47" width="4" height="12"/></g></svg>
      ANALYSIS
    </div>
    <div class="service service--exec">
      <svg width="110" height="110" viewBox="0 0 110 110"><circle cx="55" cy="55" r="54" fill="var(--ring)"/><circle cx="55" cy="55" r="44" fill="var(--disc)"/><circle cx="47" cy="46" r="13" fill="none" stroke="#fff" stroke-width="7" stroke-dasharray="5 3"/><circle cx="47" cy="46" r="5" fill="#fff"/><rect x="55" y="56" width="20" height="20" fill="none" stroke="#fff" stroke-width="4"/><rect x="60" y="61" width="10" height="10" fill="#fff"/></svg>
      EXECUTION
    </div>
  </div>
  <div class="cover__strip cover__strip--bottom">ALL GATHERED IN ONE PLACE</div>
  <div class="cover__foot"></div>
</section>

<!-- Page 2 -->
<section class="page page--p2">
  <div class="photo photo--desk" role="img" aria-label="Photo of hands typing on a laptop beside a cup of tea"></div>
  <div class="page__header" style="left:220px"><div class="page__header-line"></div><div class="page__brand">Marvelund</div></div>
  <p class="p2-text p2-text--a">Lorem Ipsum is simply dummy text of the printing and typesetting industry. Lorem Ipsum has been the industry's standard dummy text ever since the 1500s, when an unknown printer took a galley of type and scrambled it to make a type specimen book. It has survived not only five centuries.</p>
  <div class="photo photo--paper" role="img" aria-label="Photo of a person reading the business section of a newspaper"></div>
  <p class="p2-text p2-text--b">Lorem Ipsum is simply dummy text of the printing and typesetting industry. Lorem Ipsum has been the industry's standard dummy text ever since the 1500s, when an unknown printer took a galley of type and scrambled it to make a type specimen book. It has survived not only five centuries, but also the leap into electronic typesetting.</p>
  <div class="page__footer"><span class="page__web"><svg width="12" height="12" viewBox="0 0 12 12" fill="none" stroke="#333"><circle cx="6" cy="6" r="5.3"/><ellipse cx="6" cy="6" rx="2.4" ry="5.3"/><line x1=".7" y1="6" x2="11.3" y2="6"/></svg>www.lindqor.com</span><span class="page__num">2</span></div>
</section>

<!-- Page 3 -->
<section class="page page--p3">
  <div class="page__header"><div class="page__header-line"></div><div class="page__brand">Marvelund</div></div>
  <h3 class="toc-title">TABLE OF CONTENT</h3>
  <ul class="toc">
    <li class="main"><span class="t">Heading Here</span><span class="lead"></span><span class="n">4</span></li>
    <li class="sub"><span class="t">Heading Here</span><span class="lead"></span><span class="n">5</span></li>
    <li class="sub"><span class="t">Heading Here</span><span class="lead"></span><span class="n">6</span></li>
    <li class="sub"><span class="t">Heading Here</span><span class="lead"></span><span class="n">7</span></li>
    <li class="sub"><span class="t">Heading Here</span><span class="lead"></span><span class="n">8</span></li>
    <li class="sub"><span class="t">Heading Here</span><span class="lead"></span><span class="n">9</span></li>
    <li class="sub"><span class="t">Heading Here</span><span class="lead"></span><span class="n">10</span></li>
    <li class="sub"><span class="t">Heading Here</span><span class="lead"></span><span class="n">11</span></li>
    <li class="main gap"><span class="t">Heading Here</span><span class="lead"></span><span class="n">12</span></li>
    <li class="sub"><span class="t">Heading Here</span><span class="lead"></span><span class="n">13</span></li>
    <li class="sub"><span class="t">Heading Here</span><span class="lead"></span><span class="n">14</span></li>
    <li class="sub"><span class="t">Heading Here</span><span class="lead"></span><span class="n">15</span></li>
    <li class="sub"><span class="t">Heading Here</span><span class="lead"></span><span class="n">16</span></li>
    <li class="sub"><span class="t">Heading Here</span><span class="lead"></span><span class="n">17</span></li>
    <li class="sub"><span class="t">Heading Here</span><span class="lead"></span><span class="n">18</span></li>
    <li class="sub"><span class="t">Heading Here</span><span class="lead"></span><span class="n">19</span></li>
  </ul>
  <div class="page__footer"><span class="page__web"><svg width="12" height="12" viewBox="0 0 12 12" fill="none" stroke="#333"><circle cx="6" cy="6" r="5.3"/><ellipse cx="6" cy="6" rx="2.4" ry="5.3"/><line x1=".7" y1="6" x2="11.3" y2="6"/></svg>www.lindqor.com</span><span class="page__num">3</span></div>
</section>

<!-- Page 4 -->
<section class="page page--p4">
  <div class="page__header"><div class="page__header-line"></div><div class="page__brand">Marvelund</div></div>
  <div class="page__body">
    <h3 class="heading">HEADING GOES HERE</h3>
    <h4 class="subheading">Sub Heading Goes Here</h4>
    <p class="copy">Lorem Ipsum is simply dummy text of the printing and typesetting industry. Lorem Ipsum has been the industry's standard dummy text ever.</p>
    <div class="block"><span class="block__tag">Text Goes Here</span><div class="block__body"><ul><li>Lorem Ipsum is simply dummy text of the printing and typesetting.</li><li>Lorem Ipsum is simply dummy text of the printing.</li><li>Lorem Ipsum is simply dummy text of the printing and typesetting.</li></ul></div></div>
    <div class="block"><span class="block__tag">Text Goes Here</span><div class="block__body"><p>Lorem Ipsum is simply dummy text of the printing and typesetting industry. Lorem Ipsum has been the industry's standard dummy text ever.</p></div></div>
    <div class="block"><span class="block__tag">Text Goes Here</span><div class="block__body"><p>Lorem Ipsum is simply dummy text of the printing and typesetting industry. Lorem Ipsum has been the industry's standard dummy text ever.</p><ul><li>Lorem Ipsum is simply dummy text of the printing and typesetting.</li><li>Lorem Ipsum is simply dummy text of the printing.</li><li>Lorem Ipsum is simply dummy text of the printing and typesetting.</li><li>Lorem Ipsum is simply dummy text of the printing.</li></ul></div></div>
    <div class="block"><span class="block__tag">Text Goes Here</span><div class="block__body"><p>Lorem Ipsum is simply dummy text of the printing and typesetting industry. Lorem Ipsum has been the industry's standard dummy text ever since the 1500s, when an unknown printer took a galley of type and scrambled it to make a type specimen book. It has survived not only five centuries, but also the leap into electronic typesetting, remaining essentially unchanged.</p><ul><li>Lorem Ipsum is simply dummy text of the printing and typesetting.</li><li>Lorem Ipsum is simply dummy text of the printing.</li><li>Lorem Ipsum is simply dummy text of the printing and typesetting.</li></ul></div></div>
  </div>
  <div class="page__footer"><span class="page__web"><svg width="12" height="12" viewBox="0 0 12 12" fill="none" stroke="#333"><circle cx="6" cy="6" r="5.3"/><ellipse cx="6" cy="6" rx="2.4" ry="5.3"/><line x1=".7" y1="6" x2="11.3" y2="6"/></svg>www.lindqor.com</span><span class="page__num">4</span></div>
</section>

<!-- Page 5 -->
<section class="page page--p5">
  <div class="page__header"><div class="page__header-line"></div><div class="page__brand">Marvelund</div></div>
  <div class="page__body">
    <h3 class="heading">HEADING GOES HERE</h3>
    <h4 class="subheading">Sub Heading Goes Here</h4>
    <p class="copy">Lorem Ipsum is simply dummy text of the printing and typesetting industry. Lorem Ipsum has been the industry's standard dummy text ever since the 1500s, when an unknown printer took a galley of type and scrambled it to make a type specimen book. It has survived not only five centuries, but also the leap into electronic typesetting, remaining essentially unchanged. It was popularised in the 1960s with the release of Tessmark sheets containing Lorem Ipsum passages, and more recently with desktop publishing software like Norvo LayoutKit including versions of Lorem Ipsum.</p>
    <div class="table-wrap">
      <span class="table-tag">Text Goes Here</span>
      <table class="data-table">
        <tr><th>Text Goes Here</th><th>Text Goes Here</th><th>Text Goes Here</th><th>Text Goes Here</th></tr>
        <tr><td>Text Goes Here</td><td>Text Goes Here</td><td>Text Goes Here</td><td>Text Goes Here</td></tr>
        <tr><td>Text Goes Here</td><td>Text Goes Here</td><td>Text Goes Here</td><td>Text Goes Here</td></tr>
        <tr><td>Text Goes Here</td><td>Text Goes Here</td><td>Text Goes Here</td><td>Text Goes Here</td></tr>
        <tr><td>Text Goes Here</td><td>Text Goes Here</td><td>Text Goes Here</td><td>Text Goes Here</td></tr>
        <tr><td>Text Goes Here</td><td>Text Goes Here</td><td>Text Goes Here</td><td>Text Goes Here</td></tr>
        <tr><td>Text Goes Here</td><td>Text Goes Here</td><td>Text Goes Here</td><td>Text Goes Here</td></tr>
      </table>
    </div>
    <p class="copy copy--after">Lorem Ipsum is simply dummy text of the printing and typesetting industry. Lorem Ipsum has been the industry's standard dummy text ever since the 1500s, when an unknown printer took a galley of type and scrambled it to make a type specimen book. It has survived not only five centuries, but also the leap into electronic typesetting, remaining essentially unchanged. It was popularised in the 1960s with the release of Tessmark sheets containing Lorem Ipsum passages, and more recently with desktop publishing software like Norvo LayoutKit including versions of Lorem Ipsum.</p>
  </div>
  <div class="page__footer"><span class="page__web"><svg width="12" height="12" viewBox="0 0 12 12" fill="none" stroke="#333"><circle cx="6" cy="6" r="5.3"/><ellipse cx="6" cy="6" rx="2.4" ry="5.3"/><line x1=".7" y1="6" x2="11.3" y2="6"/></svg>www.lindqor.com</span><span class="page__num">5</span></div>
</section>

<!-- Page 6 -->
<section class="page page--p6">
  <div class="page__header"><div class="page__header-line"></div><div class="page__brand">Marvelund</div></div>
  <div class="page__body">
    <h3 class="heading">HEADING GOES HERE</h3>
    <h4 class="subheading">Sub Heading Goes Here</h4>
    <p class="copy">Lorem Ipsum is simply dummy text of the printing and typesetting industry. Lorem Ipsum has been the industry's standard dummy text ever since the 1500s, when an unknown printer took a galley of type and scrambled it to make a type specimen book. It has survived not only five centuries, but also the leap into electronic typesetting, remaining essentially unchanged. It was popularised in the 1960s with the release of Tessmark sheets containing Lorem Ipsum passages, and more recently with desktop publishing software like Norvo LayoutKit including versions of Lorem Ipsum. Lorem Ipsum is simply dummy text of the printing and typesetting industry. Lorem Ipsum has been the industry's standard dummy text ever since the 1500s, when an unknown printer took a galley of type and scrambled it to make a type specimen book. It has survived not only five centuries, but also the leap into electronic typesetting, remaining essentially unchanged. It was popularised in the 1960s with the release of Tessmark sheets containing Lorem Ipsum passages, and more recently with desktop publishing software like Norvo LayoutKit including versions of Lorem Ipsum.</p>
    <div class="info-panel">
      <div class="info-panel__col"><svg width="44" height="44" viewBox="0 0 44 44" fill="none" stroke="#fff" stroke-width="2"><path d="M8 4h20l8 8v28H8z"/><path d="M28 4v8h8"/><path d="M15 34V26M21 34V20M27 34V24M33 34V16" stroke-width="3"/></svg>Lorem Ipsum is simply dummy text of the printing and typesetting industry. Lorem Ipsum has been the industry's standard dummy text ever since the 1500s, when an unknown printer took a galley of type and scrambled it to make a type specimen book. It has survived not only five centuries.</div>
      <div class="info-panel__col"><svg width="44" height="44" viewBox="0 0 44 44" fill="none" stroke="#fff" stroke-width="2"><path d="M8 4h20l8 8v28H8z"/><path d="M28 4v8h8"/><path d="M15 34V26M21 34V20M27 34V24M33 34V16" stroke-width="3"/></svg>Lorem Ipsum is simply dummy text of the printing and typesetting industry. Lorem Ipsum has been the industry's standard dummy text ever since the 1500s, when an unknown printer took a galley of type and scrambled it to make a type specimen book. It has survived not only five centuries.</div>
      <div class="info-panel__col"><svg width="44" height="44" viewBox="0 0 44 44" fill="none" stroke="#fff" stroke-width="2"><path d="M8 4h20l8 8v28H8z"/><path d="M28 4v8h8"/><path d="M15 34V26M21 34V20M27 34V24M33 34V16" stroke-width="3"/></svg>Lorem Ipsum is simply dummy text of the printing and typesetting industry. Lorem Ipsum has been the industry's standard dummy text ever since the 1500s, when an unknown printer took a galley of type and scrambled it to make a type specimen book. It has survived not only five centuries.</div>
    </div>
  </div>
  <div class="page__footer"><span class="page__web"><svg width="12" height="12" viewBox="0 0 12 12" fill="none" stroke="#333"><circle cx="6" cy="6" r="5.3"/><ellipse cx="6" cy="6" rx="2.4" ry="5.3"/><line x1=".7" y1="6" x2="11.3" y2="6"/></svg>www.lindqor.com</span><span class="page__num">6</span></div>
</section>
</body>
</html>
```